Young, modern, highly skilled carpenter needs business card design

I need a business card design for my construction business. Its called 'Pellwright Construction Solutions'. Im looking for a ultra modern design that incorporates P C S, the first letters of the name with only a subtle reference to carpentry. The design should reflect my high quality work and eye for detail. i have also uploaded some exmaple designs i like.

Industry/Entity Type

Construction

Requirements
Must have
• Name of business, my name, mobile number, ABN number, email address
Nice to have
• A logo incorporating the name of the business

```html
<!DOCTYPE html>
<html lang="en">
<head>
<meta charset="utf-8">
<title>Pellwright Construction Solutions – Business Card</title>
<link rel="stylesheet" href="https://fonts.googleapis.com/css2?family=Cabin:wght@400;700&display=swap">
<style>
  :root {
    --backdrop: #e6ecec;
    --kraft-light: #d3c277;
    --kraft-dark: #c4b163;
    --card-black: #1b1b1b;
    --ink-black: #111111;
    --gold: #c9b866;
  }
  * { margin: 0; padding: 0; box-sizing: border-box; }
  html, body {
    width: 1200px;
    height: 900px;
    overflow: hidden;
    background: var(--backdrop);
    font-family: "Cabin", sans-serif;
  }
  .canvas {
    position: relative;
    width: 1200px;
    height: 900px;
  }
  .card {
    position: absolute;
    width: 542px;
    height: 370px;
  }
  .card-front {
    left: 335px;
    top: 62px;
    background: radial-gradient(ellipse at 40% 35%, var(--kraft-light), var(--kraft-dark));
  }
  .front-wordmark {
    position: absolute;
    left: 63px;
    top: 258px;
    font-size: 64px;
    font-weight: 700;
    color: var(--ink-black);
    letter-spacing: 2px;
    line-height: 1;
  }
  .card-back {
    left: 336px;
    top: 460px;
    background: var(--card-black);
    color: var(--gold);
  }
  .brand-lockup {
    position: absolute;
    left: 64px;
    top: 52px;
    display: flex;
    align-items: center;
    gap: 12px;
  }
  .brand-square {
    width: 46px;
    height: 46px;
    background: var(--gold);
  }
  .brand-name {
    font-size: 18px;
    font-weight: 400;
    letter-spacing: 0.3px;
    text-transform: uppercase;
    color: var(--gold);
    white-space: nowrap;
  }
  .contact-details {
    position: absolute;
    left: 67px;
    top: 220px;
    list-style: none;
    font-size: 19px;
    line-height: 26.5px;
    color: var(--gold);
  }
</style>
</head>
<body>
  <main class="canvas">
    <section class="card card-front" aria-label="Card front">
      <div class="front-wordmark">PCS</div>
    </section>

    <section class="card card-back" aria-label="Card back">
      <div class="brand-lockup">
        <div class="brand-square"></div>
        <div class="brand-name">Pellwright Construction Solutions</div>
      </div>
      <ul class="contact-details">
        <li class="contact-name">Liam Pellwright</li>
        <li class="contact-email">M: liam_pellwright@mailbox.com</li>
        <li class="contact-phone">T: 0491570156</li>
        <li class="contact-abn">ABN: 47 218 593 604</li>
      </ul>
    </section>
  </main>
</body>
</html>
```